Bref créative
LARCHMONT ADVISORY
"Where Your Concern Is Our Focus"
Professional
Marisol Quade
2417 Birchwood Lane, Suite 208
P.O. Box 3782
Fairhaven, AL 36197
support@larchmontadvisory.example
larchmontadvisory.example
please incorporate center logo from the website (the one with the green and black writing) thanks
for those who needed ai

```html
<!DOCTYPE html>
<html lang="en">
<head>
<meta charset="utf-8">
<title>Larchmont Advisory – Stationery</title>
<link href="https://fonts.googleapis.com/css2?family=Open+Sans:wght@400;600;700&display=swap" rel="stylesheet">
<style>
  :root {
    --bg: #3b2c24;
    --paper: #ffffff;
    --green: #0f7a3c;
    --green-dark: #07401f;
    --green-light: #2fa25c;
    --ink: #111111;
    --text: #444444;
    --muted: #777777;
  }
  * { margin: 0; padding: 0; box-sizing: border-box; }
  html, body { width: 1200px; height: 897px; overflow: hidden; }
  body { background: var(--bg); font-family: "Open Sans", Arial, sans-serif; position: relative; }

  .sheet { position: absolute; background: var(--paper); overflow: hidden; }
  .sheet svg.header { position: absolute; left: 0; top: 0; display: block; }

  .brand {
    position: absolute; display: flex; align-items: center; gap: 5px;
    color: var(--green); font-weight: 700; line-height: 1.1;
  }
  .brand-dot { border-radius: 50%; background: var(--green); flex: none; }

  /* Letterhead */
  .letterhead { left: 97px; top: 116px; width: 472px; height: 611px; }
  .letterhead .brand { left: 22px; top: 138px; font-size: 11px; }
  .letterhead .brand-dot { width: 12px; height: 12px; }
  .letter-body {
    position: absolute; left: 24px; top: 172px; width: 424px;
    font-size: 5.6px; line-height: 1.6; color: var(--text);
  }
  .letter-body p { margin-bottom: 8px; }
  .letter-body .recipient { margin-bottom: 10px; }
  .letter-footer {
    position: absolute; left: 24px; right: 24px; bottom: 22px;
    font-size: 4.6px; color: var(--muted); text-align: center; white-space: nowrap;
  }
  .letter-footer b { color: var(--green); font-weight: 600; }

  /* Business card */
  .card { left: 599px; top: 133px; width: 375px; height: 214px; border-radius: 10px; }
  .card .brand { left: 24px; top: 96px; font-size: 12px; }
  .card .brand-dot { width: 13px; height: 13px; }
  .card-contact {
    position: absolute; left: 172px; top: 96px;
    font-size: 6.6px; line-height: 1.5; color: var(--text);
  }
  .card-name { font-size: 14px; font-weight: 700; color: var(--green); margin-bottom: 4px; }
  .card-contact .label { color: var(--green); font-weight: 700; }

  /* Envelope front */
  .envelope-front { left: 601px; top: 388px; width: 373px; height: 189px; }
  .envelope-front .brand { left: 14px; top: 32px; font-size: 8px; }
  .envelope-front .brand-dot { width: 9px; height: 9px; }
  .return-address {
    position: absolute; left: 104px; top: 34px;
    font-size: 5.5px; line-height: 1.5; color: var(--text);
  }

  /* Envelope back */
  .envelope-back { left: 601px; top: 601px; width: 373px; height: 219px; }
  .flap-mark {
    position: absolute; left: 50%; top: 30px; transform: translateX(-50%);
    width: 58px; height: 58px; border-radius: 50%; background: var(--paper);
    display: flex; align-items: center; justify-content: center; text-align: center;
    color: var(--green); font-weight: 700; font-size: 7px; line-height: 1.15;
  }
</style>
</head>
<body>

  <!-- Letterhead -->
  <section class="sheet letterhead">
    <svg class="header" width="472" height="140" viewBox="0 0 472 140" aria-hidden="true">
      <defs>
        <linearGradient id="lh-green" x1="0" y1="0" x2="1" y2="1">
          <stop offset="0" stop-color="var(--green-light)"/>
          <stop offset="0.6" stop-color="var(--green)"/>
          <stop offset="1" stop-color="var(--green-dark)"/>
        </linearGradient>
      </defs>
      <path d="M0 0 H472 V34 Q270 48 150 78 Q60 100 0 124 Z" fill="url(#lh-green)"/>
      <path d="M0 134 Q70 104 160 86 Q290 60 472 48" fill="none" stroke="var(--ink)" stroke-width="6"/>
    </svg>
    <div class="brand"><span class="brand-dot"></span><span>LARCHMONT<br>ADVISORY</span></div>

    <div class="letter-body">
      <p class="recipient">Daniel Hollis<br>120 Lang Street<br>Fairhaven, Alabama</p>
      <p>Dear Mr. Hollis,</p>
      <p>Thank you for choosing our team to guide your financial planning this year. We have reviewed your accounts and prepared a clear summary of options that fit your goals, your timeline and your comfort with risk.</p>
      <p>Our advisors will meet with you to explain each step and answer every question. We believe good planning starts with listening, and we will keep you informed as your needs change.</p>
      <p>Please call our office to arrange a convenient time. We look forward to working with you and helping you build a secure future for you and your family.</p>
      <p>Thank you again for your trust.</p>
      <p>Yours sincerely,<br>Marisol Quade</p>
    </div>

    <footer class="letter-footer">
      2417 Birchwood Lane, Suite 208 · P.O. Box 3782 · Fairhaven, AL 36197 · P: (334) 555-0148 · <b>support@larchmontadvisory.example</b> · <b>larchmontadvisory.example</b>
    </footer>
  </section>

  <!-- Business card -->
  <section class="sheet card">
    <svg class="header" width="375" height="100" viewBox="0 0 375 100" aria-hidden="true">
      <defs>
        <linearGradient id="card-green" x1="0" y1="0" x2="1" y2="1">
          <stop offset="0" stop-color="var(--green-light)"/>
          <stop offset="0.6" stop-color="var(--green)"/>
          <stop offset="1" stop-color="var(--green-dark)"/>
        </linearGradient>
      </defs>
      <path d="M0 0 H375 V26 Q220 32 120 52 Q50 66 0 86 Z" fill="url(#card-green)"/>
      <path d="M0 95 Q60 72 130 62 Q240 44 375 40" fill="none" stroke="var(--ink)" stroke-width="5"/>
    </svg>
    <div class="brand"><span class="brand-dot"></span><span>LARCHMONT<br>ADVISORY</span></div>
    <div class="card-contact">
      <div class="card-name">Marisol Quade</div>
      2417 Birchwood Lane, Suite 208<br>
      P.O. Box 3782<br>
      Fairhaven, AL 36197<br>
      <span class="label">P:</span> (334) 555-0148<br>
      <span class="label">E:</span> support@larchmontadvisory.example<br>
      <span class="label">W:</span> larchmontadvisory.example
    </div>
  </section>

  <!-- Envelope front -->
  <section class="sheet envelope-front">
    <div class="brand"><span class="brand-dot"></span><span>LARCHMONT<br>ADVISORY</span></div>
    <div class="return-address">
      2417 Birchwood Lane, Suite 208<br>
      P.O. Box 3782<br>
      Fairhaven, AL 36197
    </div>
  </section>

  <!-- Envelope back -->
  <section class="sheet envelope-back">
    <svg class="header" width="373" height="140" viewBox="0 0 373 140" aria-hidden="true">
      <defs>
        <radialGradient id="flap-green" cx="0.5" cy="0.4" r="0.6">
          <stop offset="0" stop-color="var(--green-light)"/>
          <stop offset="0.5" stop-color="var(--green)"/>
          <stop offset="1" stop-color="var(--green-dark)"/>
        </radialGradient>
      </defs>
      <path d="M0 0 H373 Q320 8 270 60 Q225 110 186 112 Q148 110 103 60 Q53 8 0 0 Z" fill="url(#flap-green)"/>
      <path d="M0 0 Q56 14 108 66 Q150 118 186 120 Q222 118 265 66 Q317 14 373 0" fill="none" stroke="var(--ink)" stroke-width="4"/>
    </svg>
    <div class="flap-mark">LARCHMONT<br>ADVISORY</div>
  </section>

</body>
</html>
```